Postcard Design

I sell hearing aids online. My company is maplewood hearing aids. we are looking for a referral post card, 5.47" x 4.21" front and back

The hearings I sell are 50 to 75% less in cost than most places.

I am going to put this post card, 10of them in an envelope with a letter, 1st thanking them for their business, 2nd asking them to hand these out to friends and family.

I uploaded two cards. I think file 2 would be easier - I need to take action.

Target Market(s)

Baby Boomers, Seniors, average age 66 years old. Retired, semi retired. likes to save money. Male 52% female 48%

Industry/Entity Type

Business

Font styles to use
Sans Serif

Colors
4683bc
32a6d7
ffffff
0255a3

Requirements
Must have
• Easy to read. Black letters on white background, Arial text, large, easy to read. Seniors have bad eyesight.
Should not have
• anything other than arial or sans serif text, needs to be easy to read.

```html
<!DOCTYPE html>
<html lang="en">
<head>
<meta charset="utf-8">
<title>Maplewood Hearing Aids – Referral Postcard</title>
<link rel="stylesheet" href="https://fonts.googleapis.com/css2?family=Arimo:wght@400;700&display=swap">
<style>
  :root {
    --blue-mid: #4683bc;
    --blue-sky: #32a6d7;
    --blue-deep: #0255a3;
    --blue-pale: #cfe6f5;
    --white: #ffffff;
    --ink: #111111;
    --stage: #e9edf1;
    --rule: #9aa4ad;
  }
  * { box-sizing: border-box; margin: 0; padding: 0; }
  html, body { width: 807px; height: 1200px; overflow: hidden; }
  body {
    background: var(--stage);
    font-family: "Arimo", Arial, sans-serif;
    color: var(--ink);
    position: relative;
  }
  .postcard {
    position: absolute;
    left: 67px;
    width: 686px;
    height: 574px;
    background: var(--white);
    overflow: hidden;
    box-shadow: 0 2px 10px rgba(0,0,0,.18);
  }
  .postcard--front { top: 13px; }
  .postcard--back { top: 610px; }

  /* Front */
  .front-photo {
    position: absolute; left: 0; top: 0; width: 100%; height: 420px;
    background: linear-gradient(160deg, #dfe8ef 0%, #c9b79a 45%, #a88f73 70%, #d9dfe4 100%);
  }
  .front-waves { position: absolute; left: 0; top: 300px; width: 100%; height: 150px; }
  .brand {
    position: absolute; left: 18px; top: 30px;
    display: flex; flex-direction: column; gap: 6px;
  }
  .brand__name {
    display: flex; align-items: center; gap: 10px;
    font-size: 30px; font-weight: 700; color: var(--blue-deep);
    text-transform: uppercase; letter-spacing: .5px;
  }
  .brand__dot { width: 22px; height: 22px; border-radius: 50%; background: var(--blue-sky); }
  .brand__tagline {
    background: var(--blue-deep); color: var(--white);
    font-size: 17px; font-weight: 700; padding: 4px 10px;
  }
  .front-headline {
    position: absolute; left: 0; right: 0; top: 478px;
    text-align: center; font-size: 52px; font-weight: 700; letter-spacing: -.5px;
  }

  /* Back */
  .back-swoosh { position: absolute; left: 0; top: 0; width: 100%; height: 60px; }
  .back-wave { position: absolute; right: 0; bottom: 0; width: 100%; height: 110px; }
  .back-copy {
    position: absolute; left: 30px; top: 52px; width: 420px;
    font-size: 15.5px; line-height: 1.25;
  }
  .back-copy p + p { margin-top: 10px; }
  .questions { list-style: none; margin: 14px 0 16px; }
  .questions li {
    color: var(--blue-deep); font-weight: 700; font-size: 16.5px;
    padding-left: 20px; text-indent: -20px; margin-bottom: 4px;
  }
  .questions b { color: var(--ink); display: inline-block; width: 20px; text-indent: 0; }
  .indent { margin-left: 160px; display: block; }
  .advisor-photo {
    position: absolute; left: 14px; top: 385px; width: 150px; height: 165px;
    background: linear-gradient(180deg, #c9d5de 0%, #9fb0bf 60%, #7d8f9f 100%);
  }
  .report {
    position: absolute; left: 190px; top: 430px; width: 260px;
    text-align: center; font-weight: 700; color: var(--blue-deep);
  }
  .report__label { font-size: 15px; }
  .report__url { font-size: 13px; color: var(--ink); margin-top: 3px; }
  .batteries {
    position: absolute; left: 250px; top: 495px;
    font-size: 13.5px; font-weight: 700; color: var(--blue-deep);
  }
  .address-lines { position: absolute; left: 465px; top: 255px; width: 205px; }
  .address-lines span { display: block; height: 1px; background: var(--rule); margin-bottom: 44px; }
</style>
</head>
<body>

<section class="postcard postcard--front" aria-label="Postcard front">
  <div class="front-photo" role="img" aria-label="Photo of a smiling woman hugging an elderly man"></div>
  <svg class="front-waves" viewBox="0 0 686 150" preserveAspectRatio="none" aria-hidden="true">
    <path d="M0 60 C180 10 360 120 686 30 L686 150 L0 150 Z" fill="var(--blue-pale)"/>
    <path d="M0 80 C200 40 380 140 686 55 L686 150 L0 150 Z" fill="var(--blue-sky)"/>
    <path d="M0 100 C220 70 400 150 686 85 L686 150 L0 150 Z" fill="var(--blue-deep)"/>
    <path d="M0 125 C240 100 420 150 686 118 L686 150 L0 150 Z" fill="var(--white)"/>
  </svg>
  <div class="brand">
    <div class="brand__name"><span class="brand__dot"></span>Maplewood Hearing Aids</div>
    <div class="brand__tagline">Top Quality. Lowest Prices.</div>
  </div>
  <h1 class="front-headline">Someone Cares About You</h1>
</section>

<section class="postcard postcard--back" aria-label="Postcard back">
  <svg class="back-swoosh" viewBox="0 0 686 60" preserveAspectRatio="none" aria-hidden="true">
    <path d="M0 0 L340 0 C240 10 120 22 0 40 Z" fill="var(--blue-deep)"/>
    <path d="M0 40 C120 22 240 10 340 0 L360 0 C250 14 130 30 0 50 Z" fill="var(--blue-sky)"/>
  </svg>

  <div class="back-copy">
    <p>You received this card because your friend thought you could use a little help with your hearing. If that is true, Please take few moments to answer these questions...</p>
    <ol class="questions">
      <li><b>A.</b>Do you have trouble hearing conversation in noisy places?</li>
      <li><b>B.</b>Do you turn the TV too loud?</li>
      <li><b>C.</b>Do you have trouble hearing speakers at public gatherings?</li>
      <li><b>D.</b>Do you have trouble hearing women-children's voices?</li>
    </ol>
    <p>Did you answer "YES" to any of those questions? If so, you could benefit from hearing aids. Did you know that <span class="indent">the person that gave you this card bought hearing aids online for 50 to 75% less than a local doctors office? Its true.</span></p>
  </div>

  <div class="advisor-photo" role="img" aria-label="Portrait of the company owner with his signature"></div>

  <div class="report">
    <div class="report__label">Get the FREE REPORT at:</div>
    <div class="report__url">www.MaplewoodHearingAids.com/free-report</div>
  </div>
  <div class="batteries">Get one year FREE batteries!</div>

  <div class="address-lines" aria-hidden="true"><span></span><span></span><span></span></div>

  <svg class="back-wave" viewBox="0 0 686 110" preserveAspectRatio="none" aria-hidden="true">
    <path d="M686 20 C560 70 420 95 160 110 L686 110 Z" fill="var(--blue-sky)"/>
    <path d="M686 50 C580 85 460 100 300 110 L686 110 Z" fill="var(--blue-deep)"/>
  </svg>
</section>

</body>
</html>
```